TELVA EV

We need a business card design for a new Luxury golf cart Company Telva. We manufacture and sell high end golf carts. We would like to see designs that are high end. I have the logo so really need a nice clean look.

```html
<!DOCTYPE html>
<html lang="en">
<head>
<meta charset="utf-8">
<title>Telva EV Business Cards</title>
<link href="https://fonts.googleapis.com/css2?family=Open+Sans:wght@400;600;700&display=swap" rel="stylesheet">
<style>
  :root {
    --stage: #3a3a3a;
    --card: #111111;
    --teal: #13917c;
    --text: #e8e8e8;
    --muted: #bdbdbd;
  }
  * { margin: 0; padding: 0; box-sizing: border-box; }
  html, body {
    width: 1200px; height: 801px; overflow: hidden;
    background: var(--stage);
    font-family: "Open Sans", Arial, sans-serif;
  }
  .stage {
    width: 1200px; height: 801px;
    display: flex; align-items: center; justify-content: center; gap: 40px;
  }
  .card {
    width: 540px; height: 309px;
    background: var(--card);
    border-bottom: 2px solid var(--teal);
    box-shadow: 0 10px 30px rgba(0,0,0,.45);
    position: relative;
    color: var(--text);
  }
  .wordmark {
    font-weight: 700;
    color: var(--text);
    letter-spacing: 6px;
    line-height: 1;
  }
  .card-contact { display: flex; }
  .card-contact .logo-zone {
    width: 250px; display: flex; align-items: center; justify-content: center;
  }
  .card-contact .wordmark { font-size: 40px; }
  .divider {
    width: 1px; background: var(--teal);
    margin: 70px 0 70px;
  }
  .details {
    padding: 66px 0 0 26px;
    font-size: 13.5px; line-height: 1.4;
  }
  .name {
    color: var(--teal); font-weight: 700; font-size: 18px; letter-spacing: .5px;
  }
  .title { margin-bottom: 14px; }
  .address { margin-bottom: 14px; }
  .contact-line { display: flex; align-items: center; gap: 8px; }
  .contact-line svg { width: 11px; height: 11px; flex: none; fill: var(--teal); }
  .card-front { display: flex; align-items: center; justify-content: center; }
  .card-front .wordmark { font-size: 60px; letter-spacing: 10px; }
</style>
</head>
<body>
<main class="stage">
  <section class="card card-contact">
    <div class="logo-zone"><span class="wordmark">TELVA</span></div>
    <div class="divider"></div>
    <div class="details">
      <p class="name">DARIN HOLLOWAY</p>
      <p class="title">President</p>
      <p class="address">18230 Harbor Crest Dr<br>Seal Cove CA 92700</p>
      <p class="contact-line">
        <svg viewBox="0 0 24 24"><path d="M6.6 10.8a15 15 0 0 0 6.6 6.6l2.2-2.2a1 1 0 0 1 1-.25 11.4 11.4 0 0 0 3.6.57 1 1 0 0 1 1 1V20a1 1 0 0 1-1 1A17 17 0 0 1 3 4a1 1 0 0 1 1-1h3.5a1 1 0 0 1 1 1c0 1.25.2 2.45.57 3.6a1 1 0 0 1-.25 1z"/></svg>
        555-240-6187
      </p>
      <p class="contact-line">
        <svg viewBox="0 0 24 24"><path d="M2 5h20v14H2z M2 5l10 8 10-8" fill="none" stroke="#13917c" stroke-width="2.5"/></svg>
        darin.holloway@Telva.com
      </p>
      <p class="contact-line">
        <svg viewBox="0 0 24 24"><circle cx="12" cy="12" r="10" fill="none" stroke="#13917c" stroke-width="2.5"/><path d="M2 12h20M12 2c3 3 3 17 0 20M12 2c-3 3-3 17 0 20" fill="none" stroke="#13917c" stroke-width="2"/></svg>
        www.Telva.com
      </p>
    </div>
  </section>
  <section class="card card-front">
    <span class="wordmark">TELVA</span>
  </section>
</main>
</body>
</html>
```